practice letterhead

I need a letterhead design for a new company that is a veterinary specialty company. I am conservative. I want it to look professional - not "cutesy"

I need my name, credentials, address, phone number and website/email on it.

My personal information is as follows: Lorraine Aldous, DVM, DACVIM (Neurology) Certified Veterinary Pain Practitioner (or CVPP) Certified Canine Rehabilitation Therapist (or CCRT) 1487 Marden Hwy Harlow Bay 02317 508-374-6620 lorraine.aldous@kindpawspecialty.com www.kindpawspecialty.com

```html
<!DOCTYPE html>
<html lang="en">
<head>
<meta charset="utf-8">
<title>Kind Paw Veterinary Specialty Center – Letterhead</title>
<link rel="stylesheet" href="https://fonts.googleapis.com/css2?family=Roboto:ital,wght@0,400;0,500;0,700;1,700&display=swap">
<style>
  :root {
    --canvas-bg: #e9e7e3;
    --paper: #ffffff;
    --navy: #1f2c3a;
    --teal: #6c8f85;
    --teal-dark: #2f5d5f;
    --shadow-grey: #d9dcdc;
    --white: #ffffff;
  }
  * { box-sizing: border-box; margin: 0; padding: 0; }
  html, body {
    width: 1132px;
    height: 1200px;
    overflow: hidden;
    background: var(--canvas-bg);
  }
  body {
    font-family: "Roboto", Arial, sans-serif;
    position: relative;
  }
  .letterhead {
    position: absolute;
    left: 126px;
    top: 30px;
    width: 880px;
    height: 1140px;
    background: var(--paper);
    box-shadow: 0 6px 22px rgba(0, 0, 0, 0.18);
    overflow: hidden;
  }

  /* Header */
  .brand {
    position: absolute;
    left: 0;
    top: 0;
    width: 380px;
    height: 130px;
  }
  .brand-swoosh {
    position: absolute;
    left: 0;
    top: 0;
  }
  .brand-lockup {
    position: absolute;
    left: 34px;
    top: 28px;
    display: flex;
    align-items: center;
    gap: 14px;
  }
  .brand-dot {
    width: 56px;
    height: 56px;
    border-radius: 50%;
    background: var(--teal-dark);
    flex: none;
  }
  .brand-name {
    color: var(--teal);
    font-weight: 500;
    font-size: 21px;
    line-height: 1.12;
    letter-spacing: 0.2px;
  }

  .sender {
    position: absolute;
    right: 40px;
    top: 40px;
    text-align: right;
    color: var(--navy);
  }
  .sender-name {
    font-weight: 700;
    font-size: 22px;
    letter-spacing: 0.5px;
    text-transform: uppercase;
    margin-bottom: 4px;
  }
  .sender-credentials {
    font-weight: 700;
    font-style: italic;
    font-size: 12.5px;
    line-height: 1.45;
  }

  /* Footer band */
  .contact-band {
    position: absolute;
    left: 0;
    bottom: 0;
    width: 100%;
    height: 112px;
    background: var(--teal);
  }
  .contact-list {
    position: absolute;
    left: 36px;
    top: 24px;
    display: grid;
    grid-template-columns: 250px 330px;
    row-gap: 22px;
    list-style: none;
  }
  .contact-item {
    display: flex;
    align-items: center;
    gap: 12px;
    color: var(--white);
    font-weight: 700;
    font-size: 15px;
    white-space: nowrap;
  }
  .contact-item svg {
    width: 20px;
    height: 20px;
    flex: none;
  }
  .band-mark {
    position: absolute;
    right: 32px;
    top: 8px;
    width: 96px;
    height: 96px;
    border-radius: 50%;
    background: var(--white);
    border: 5px solid var(--teal-dark);
    display: flex;
    align-items: center;
    justify-content: center;
    text-align: center;
    color: var(--teal-dark);
    font-weight: 500;
    font-size: 13px;
    line-height: 1.15;
  }
</style>
</head>
<body>
  <main class="letterhead">
    <header>
      <div class="brand">
        <svg class="brand-swoosh" width="380" height="130" viewBox="0 0 380 130" aria-hidden="true">
          <defs>
            <linearGradient id="swooshFade" x1="0" x2="1" y1="0" y2="0">
              <stop offset="0" stop-color="var(--shadow-grey)"/>
              <stop offset="1" stop-color="var(--shadow-grey)" stop-opacity="0"/>
            </linearGradient>
          </defs>
          <path d="M0 104 C120 112 250 112 350 102 C250 122 120 128 0 124 Z" fill="url(#swooshFade)"/>
        </svg>
        <div class="brand-lockup">
          <span class="brand-dot"></span>
          <p class="brand-name">Kind Paw Veterinary<br>Specialty Center</p>
        </div>
      </div>

      <div class="sender">
        <h1 class="sender-name">Lorraine Aldous,</h1>
        <p class="sender-credentials">
          DVM, DACVIM (Neurology)<br>
          Certified Veterinary Pain Practitioner (or CVPP)<br>
          Certified Canine Rehabilitation Therapist (or CCRT)
        </p>
      </div>
    </header>

    <footer class="contact-band">
      <ul class="contact-list">
        <li class="contact-item">
          <svg viewBox="0 0 24 24" aria-hidden="true"><rect x="2" y="2" width="20" height="20" rx="4" fill="var(--white)"/><path d="M8 6c-1 1-1.5 2 0 5s4 5.5 6 6.5 3-0.5 4-1.5l-2-2.5-2 1c-1.5-1-3-2.5-4-4l1-2z" fill="var(--teal)"/></svg>
          508-374-6620
        </li>
        <li class="contact-item">
          <svg viewBox="0 0 24 24" aria-hidden="true"><path d="M12 1C7.6 1 4.5 4.2 4.5 8.4 4.5 14 12 23 12 23s7.5-9 7.5-14.6C19.5 4.2 16.4 1 12 1z" fill="var(--white)"/><circle cx="12" cy="8.5" r="3" fill="var(--teal)"/></svg>
          1487 Marden Hwy. Harlow Bay 02317
        </li>
        <li class="contact-item">
          <svg viewBox="0 0 24 24" aria-hidden="true"><circle cx="12" cy="12" r="10" fill="none" stroke="var(--white)" stroke-width="2"/><ellipse cx="12" cy="12" rx="4.5" ry="10" fill="none" stroke="var(--white)" stroke-width="2"/><path d="M2 12h20M4 7h16M4 17h16" stroke="var(--white)" stroke-width="2"/></svg>
          www.kindpawspecialty.com
        </li>
        <li class="contact-item">
          <svg viewBox="0 0 24 24" aria-hidden="true"><rect x="2" y="5" width="20" height="14" rx="1.5" fill="none" stroke="var(--white)" stroke-width="2"/><path d="M2.5 6l9.5 7 9.5-7" fill="none" stroke="var(--white)" stroke-width="2"/></svg>
          lorraine.aldous@kindpawspecialty.com
        </li>
      </ul>
      <div class="band-mark">Kind Paw</div>
    </footer>
  </main>
</body>
</html>
```